Service business needs Business Card Design

Looking to create a new business card design that is both professional and unique the can highlight the many services we offer throughout the seasons. Our tagline is "The Cobalt Advantage"
Licensed & Insured: HC731462 has to be small and on the back side of the card.
On the Front:
FirstName LastName
Title
We offer the following services:
Deck Repair and Maintenance
Deck Cleaning and Staining/Painting
Power Washing/House Washing
Landscape Lighting Installation
Christmas Lighting Installation

```html
<!DOCTYPE html>
<html lang="en">
<head>
<meta charset="utf-8">
<title>Halvorn Services – Business Card</title>
<link rel="stylesheet" href="https://fonts.googleapis.com/css2?family=Montserrat:wght@500;600;700&family=Arimo:wght@400&display=swap">
<style>
  :root {
    --stage: #1c1c1e;
    --navy: #124679;
    --brand-blue: #134d8c;
    --back-blue: #2a8ae6;
    --sky: #4cc3f0;
    --ink-grey: #5a5f66;
    --paper: #ffffff;
    --on-navy: #ffffff;
  }
  * { box-sizing: border-box; margin: 0; padding: 0; }
  html, body { width: 1200px; height: 852px; overflow: hidden; }
  body {
    background: var(--stage);
    display: flex;
    flex-direction: column;
    align-items: center;
    justify-content: center;
    gap: 40px;
    font-family: "Montserrat", Arial, sans-serif;
  }
  .card {
    width: 640px;
    height: 366px;
    border-radius: 22px;
    position: relative;
    overflow: hidden;
  }

  /* Back side */
  .card--back {
    background: var(--navy);
    display: flex;
    flex-direction: column;
    align-items: center;
    justify-content: center;
    gap: 34px;
  }
  .brand-mark {
    display: flex;
    align-items: center;
    gap: 14px;
  }
  .brand-mark__dot {
    width: 22px; height: 22px;
    border-radius: 50%;
    background: currentColor;
    flex: none;
  }
  .brand-mark__name {
    font-weight: 700;
    font-size: 42px;
    letter-spacing: 3px;
    text-transform: uppercase;
    line-height: 1;
  }
  .card--back .brand-mark { color: var(--back-blue); }
  .tagline {
    color: var(--on-navy);
    font-weight: 600;
    font-size: 20px;
    letter-spacing: 3px;
    text-transform: uppercase;
  }

  /* Front side */
  .card--front {
    background: var(--paper);
    display: flex;
    align-items: center;
    padding-bottom: 30px;
  }
  .card--front .brand-mark {
    color: var(--brand-blue);
    width: 300px;
    justify-content: center;
  }
  .card--front .brand-mark__name { font-size: 34px; }
  .divider {
    width: 1.5px;
    height: 200px;
    background: var(--brand-blue);
    margin-right: 30px;
  }
  .contact { flex: 1; }
  .person__name {
    color: var(--brand-blue);
    font-weight: 700;
    font-size: 28px;
    letter-spacing: 0.5px;
    text-transform: uppercase;
    line-height: 1.2;
  }
  .person__title {
    color: var(--ink-grey);
    font-weight: 500;
    font-size: 17px;
    letter-spacing: 1px;
    text-transform: uppercase;
    margin: 2px 0 12px;
  }
  .services { list-style: none; }
  .services__item {
    font-family: "Arimo", Arial, sans-serif;
    color: var(--ink-grey);
    font-size: 15px;
    line-height: 23px;
    display: flex;
    align-items: center;
    gap: 9px;
    white-space: nowrap;
  }
  .services__item::before {
    content: "";
    width: 10px; height: 10px;
    border-radius: 50%;
    background: var(--brand-blue);
    flex: none;
  }
  .licence {
    position: absolute;
    left: 330px;
    bottom: 30px;
    font-family: "Arimo", Arial, sans-serif;
    font-size: 14px;
    line-height: 16px;
    color: var(--brand-blue);
    white-space: nowrap;
  }
  .licence__number { color: var(--ink-grey); }
  .accent-stripe {
    position: absolute;
    right: 0;
    bottom: 52px;
    width: 96px;
    height: 12px;
    background: var(--sky);
  }
</style>
</head>
<body>
  <section class="card card--back" aria-label="Card back">
    <div class="brand-mark">
      <span class="brand-mark__dot"></span>
      <span class="brand-mark__name">Halvorn Services</span>
    </div>
    <p class="tagline">The Cobalt Advantage</p>
  </section>

  <section class="card card--front" aria-label="Card front">
    <div class="brand-mark">
      <span class="brand-mark__dot"></span>
      <span class="brand-mark__name">Halvorn<br>Services</span>
    </div>
    <div class="divider"></div>
    <div class="contact">
      <h1 class="person__name">Dorian Pell</h1>
      <p class="person__title">Director</p>
      <ul class="services">
        <li class="services__item">Deck Repair and Maintenance</li>
        <li class="services__item">Deck Cleaning and Staining/Painting</li>
        <li class="services__item">Power Washing/House Washing</li>
        <li class="services__item">Landscape Lighting Installation</li>
        <li class="services__item">Christmas Lighting Installation</li>
      </ul>
    </div>
    <p class="licence">Licensed &amp; Insured: <span class="licence__number">HC731462</span></p>
    <div class="accent-stripe"></div>
  </section>
</body>
</html>
```